We have developed a fully functional App called Corvalink. However, it requires a nicer GUI. You can see screenshots of our App on www.corvalink-example.com under "Tutorial". For those of you with Android, you can also install it. When you go to Corvalink-example.com, your phone will automatically redirect you to download. From there, you'll get a better idea of what our App looks like and how your design can make it way better. Please note we expect a design idea for most screens (there's about 8 screens) but do just one screen first and if you win, you can do the other 8 after.

Target Market(s)

People looking for dating / flirting

Industry/Entity Type

Android

Requirements
Must have
• sleek looking

```html
<!DOCTYPE html>
<html lang="en">
<head>
<meta charset="utf-8">
<title>Corvalink – Browse</title>
<link rel="stylesheet" href="https://fonts.googleapis.com/css2?family=Open+Sans:wght@300;400&family=Roboto:wght@400&display=swap">
<style>
  :root {
    --page-bg: #e2e2e2;
    --screen-bg: #e6e6e6;
    --statusbar-bg: #1c1c1c;
    --status-blue: #33b5e5;
    --card: #626262;
    --card-faded: #d3d3d3;
    --card-faded-text: #bdbdbd;
    --text-main: #ffffff;
    --text-sub: #a9a9a9;
    --dot-yellow: #f2c500;
    --dot-green: #8cc63f;
    --dot-red: #e0392f;
  }
  * { box-sizing: border-box; margin: 0; padding: 0; }
  html, body { width: 1200px; height: 1200px; overflow: hidden; }
  body {
    background: var(--page-bg);
    font-family: "Open Sans", Arial, sans-serif;
    position: relative;
  }
  .screen {
    position: absolute;
    left: 285px; top: 40px;
    width: 630px; height: 1120px;
    background: var(--screen-bg);
    overflow: hidden;
    box-shadow: 0 10px 40px rgba(0,0,0,0.12);
  }
  .status-bar {
    position: absolute; left: 0; top: 0; right: 0;
    height: 40px;
    background: var(--statusbar-bg);
    display: flex; align-items: center; justify-content: flex-end;
    gap: 6px; padding-right: 14px;
    z-index: 5;
  }
  .status-bar svg { display: block; }
  .status-time {
    font-family: "Roboto", Arial, sans-serif;
    color: var(--status-blue);
    font-size: 22px;
    margin-left: 4px;
  }
  .feed { position: absolute; left: 0; top: 40px; right: 0; bottom: 0; }
  .card {
    position: absolute;
    width: 240px; height: 232px;
    background: var(--card);
    border-radius: 10px;
    color: var(--text-main);
  }
  .card--faded {
    background: var(--card-faded);
    filter: blur(2px);
    color: var(--card-faded-text);
  }
  .card__star { position: absolute; top: 18px; right: 20px; }
  .card__info { position: absolute; left: 24px; bottom: 22px; right: 10px; white-space: nowrap; }
  .card__name {
    display: flex; align-items: center; gap: 10px;
    font-weight: 300; font-size: 25px; line-height: 1.2;
  }
  .card__dot {
    width: 11px; height: 11px; border-radius: 50%;
    border: 2px solid currentColor; flex: none;
  }
  .dot--yellow { color: var(--dot-yellow); }
  .dot--green { color: var(--dot-green); }
  .dot--red { color: var(--dot-red); }
  .card__about { font-size: 12px; font-weight: 300; color: var(--text-sub); margin-top: 8px; }
  .card__age { color: var(--text-main); font-weight: 400; }
  .card--faded .card__about, .card--faded .card__age { color: var(--card-faded-text); }
</style>
</head>
<body>
<main class="screen">
  <header class="status-bar">
    <svg width="24" height="20" viewBox="0 0 24 20" aria-label="Wi-Fi"><path d="M12 19 L0 5 A18 18 0 0 1 24 5 Z" fill="var(--status-blue)"/></svg>
    <svg width="18" height="20" viewBox="0 0 18 20" aria-label="Signal"><path d="M18 1 V19 H0 Z" fill="var(--status-blue)"/></svg>
    <svg width="11" height="22" viewBox="0 0 11 22" aria-label="Battery"><rect x="3" y="0" width="5" height="3" fill="var(--status-blue)"/><rect x="0" y="2" width="11" height="20" rx="1" fill="var(--status-blue)"/></svg>
    <span class="status-time">13:07</span>
  </header>

  <section class="feed">
    <!-- depth layer -->
    <div class="card card--faded" style="left:220px;top:-10px;width:180px;height:80px;"><div class="card__info"><div class="card__name" style="font-size:16px">Nicole</div></div></div>
    <div class="card card--faded" style="left:120px;top:90px;width:200px;height:220px;"><div class="card__info"><div class="card__name" style="font-size:16px">Andrea</div></div></div>
    <div class="card card--faded" style="left:420px;top:250px;width:190px;height:190px;"><div class="card__info"><div class="card__name" style="font-size:16px">Maria</div></div></div>
    <div class="card card--faded" style="left:60px;top:320px;width:200px;height:210px;"></div>
    <div class="card card--faded" style="left:250px;top:330px;width:190px;height:230px;"><div class="card__info"><div class="card__name" style="font-size:16px">Laura</div><div class="card__about">Wants to chat</div></div></div>
    <div class="card card--faded" style="left:440px;top:440px;width:190px;height:120px;"></div>
    <div class="card card--faded" style="left:330px;top:660px;width:200px;height:210px;"><div class="card__info"><div class="card__name" style="font-size:16px">Barbara</div></div></div>
    <div class="card card--faded" style="left:90px;top:720px;width:200px;height:90px;"></div>
    <div class="card card--faded" style="left:460px;top:920px;width:180px;height:160px;"></div>

    <!-- foreground cards -->
    <article class="card" style="left:-70px;top:0;width:210px;height:230px;">
      <svg class="card__star" width="22" height="22" viewBox="0 0 24 24"><path d="M12 2.5l2.8 6.1 6.6.7-4.9 4.5 1.4 6.6L12 17l-5.9 3.4 1.4-6.6-4.9-4.5 6.6-.7z" fill="none" stroke="#fff" stroke-width="1.4" stroke-linejoin="round"/></svg>
      <div class="card__info"><div class="card__about">Looking for men <span class="card__age">18</span></div></div>
    </article>

    <article class="card" style="left:540px;top:-60px;width:160px;height:120px;">
      <div class="card__info" style="bottom:14px;left:16px">
        <div class="card__name"><span class="card__dot dot--green"></span>Jenny</div>
        <div class="card__about" style="margin-top:2px">Looking</div>
      </div>
    </article>

    <article class="card" style="left:210px;top:110px;">
      <svg class="card__star" width="22" height="22" viewBox="0 0 24 24"><path d="M12 2.5l2.8 6.1 6.6.7-4.9 4.5 1.4 6.6L12 17l-5.9 3.4 1.4-6.6-4.9-4.5 6.6-.7z" fill="none" stroke="#fff" stroke-width="1.4" stroke-linejoin="round"/></svg>
      <div class="card__info">
        <div class="card__name"><span class="card__dot dot--yellow"></span>Barbara</div>
        <div class="card__about">Open for FWB with men <span class="card__age">25-28</span></div>
      </div>
    </article>

    <article class="card" style="left:20px;top:420px;width:260px;">
      <svg class="card__star" width="22" height="22" viewBox="0 0 24 24"><path d="M12 2.5l2.8 6.1 6.6.7-4.9 4.5 1.4 6.6L12 17l-5.9 3.4 1.4-6.6-4.9-4.5 6.6-.7z" fill="none" stroke="#fff" stroke-width="1.4" stroke-linejoin="round"/></svg>
      <div class="card__info">
        <div class="card__name"><span class="card__dot dot--green"></span>Jessica</div>
        <div class="card__about">Wants to chat with men <span class="card__age">20-25</span></div>
      </div>
    </article>

    <article class="card" style="left:450px;top:480px;width:250px;">
      <div class="card__info">
        <div class="card__name"><span class="card__dot dot--red"></span>Bonnie</div>
        <div class="card__about">Wants to chat with men <span class="card__age">21-30</span></div>
      </div>
    </article>

    <article class="card" style="left:220px;top:800px;">
      <svg class="card__star" width="22" height="22" viewBox="0 0 24 24"><path d="M12 2.5l2.8 6.1 6.6.7-4.9 4.5 1.4 6.6L12 17l-5.9 3.4 1.4-6.6-4.9-4.5 6.6-.7z" fill="none" stroke="#fff" stroke-width="1.4" stroke-linejoin="round"/></svg>
    </article>
  </section>
</main>
</body>
</html>
```